Advert for Services that we offer

Bolt Remova Ltd need an design to represent what we do in a modern way by showing an image with a brief description and the use of corporate logo the information we will proved vie a doc file and this is to be presented in a modern way. This design will be for print & web. we have done our own design and its not great i have put this in the file repository

Target Market(s)

Motor trade

Font styles to use
Sans Serif

Colors

Designer to choose colors to be used in the design.

Requirements
Must have
• Company colour scheme as per logo within the files uploaded.
• and a small boarder to isolate it from the rest of the articles.
Nice to have
• Modern font
Should not have
• Old style font

```html
<!DOCTYPE html>
<html lang="en">
<head>
<meta charset="utf-8">
<title>Bolt Remova Ltd – Product Testing &amp; Analysis</title>
<link href="https://fonts.googleapis.com/css2?family=Montserrat:wght@400;500;700&display=swap" rel="stylesheet">
<style>
  :root {
    --page-bg: #e8e9ea;
    --card-white: #ffffff;
    --brand-blue: #2270bd;
    --brand-blue-deep: #1d63ae;
    --pill-blue: #2a5f97;
    --rule-blue: #6fa3d6;
    --contact-grey: #dadada;
    --ink-dark: #1e1e1e;
    --ink-white: #ffffff;
  }
  html, body {
    margin: 0;
    padding: 0;
    width: 1200px;
    height: 966px;
    overflow: hidden;
    background: var(--page-bg);
    font-family: "Montserrat", Arial, sans-serif;
  }
  .advert {
    position: absolute;
    left: 20px;
    top: 74px;
    width: 1160px;
    height: 819px;
    display: block;
    filter: drop-shadow(0 6px 10px rgba(0,0,0,0.18));
  }
  .heading { font-size: 28px; fill: var(--ink-white); letter-spacing: 0.6px; }
  .service { font-size: 28px; fill: var(--ink-white); letter-spacing: 1.2px; }
  .strong { font-weight: 700; }
  .light { font-weight: 400; }
  .company-name { font-size: 31px; font-weight: 700; fill: var(--brand-blue); letter-spacing: 0.5px; }
  .phone { font-size: 24px; font-weight: 700; fill: var(--ink-dark); }
  .web { font-size: 20px; font-weight: 400; fill: var(--ink-dark); letter-spacing: 0.4px; }
</style>
</head>
<body>
<svg class="advert" viewBox="0 0 1220 861" xmlns="http://www.w3.org/2000/svg" aria-label="Bolt Remova Ltd product testing and analysis advert">
  <defs>
    <linearGradient id="panelGradient" x1="0" y1="0" x2="1" y2="1">
      <stop offset="0" stop-color="#2a78c4"/>
      <stop offset="1" stop-color="#1d64b0"/>
    </linearGradient>
    <linearGradient id="photoGradient" x1="0" y1="0" x2="0.6" y2="1">
      <stop offset="0" stop-color="#c9b3a2"/>
      <stop offset="0.35" stop-color="#8c8f95"/>
      <stop offset="0.65" stop-color="#6f5b55"/>
      <stop offset="0.85" stop-color="#a7481f"/>
      <stop offset="1" stop-color="#3c3f46"/>
    </linearGradient>
  </defs>

  <!-- card -->
  <rect class="card-frame" x="0" y="0" width="1220" height="861" fill="var(--card-white)"/>

  <!-- blue services panel -->
  <polygon class="services-panel" points="9,9 882,9 659,556 9,556" fill="url(#panelGradient)"/>

  <text class="heading" x="59" y="86"><tspan class="strong">PRODUCT TESTING</tspan><tspan class="light"> &amp; </tspan><tspan class="strong">ANALYSIS</tspan></text>
  <line class="heading-rule" x1="55" y1="108" x2="564" y2="108" stroke="var(--rule-blue)" stroke-width="1.2"/>

  <g class="service-list">
    <g class="service-item">
      <path d="M9 142 H540 A24 24 0 0 1 540 190 H9 Z" fill="var(--pill-blue)" opacity="0.85"/>
      <circle cx="35" cy="170" r="6.5" fill="var(--ink-white)"/>
      <text class="service" x="59" y="180"><tspan class="strong">METALLURGICAL</tspan><tspan class="light"> TESTING</tspan></text>
    </g>
    <g class="service-item">
      <path d="M9 199 H540 A24 24 0 0 1 540 247 H9 Z" fill="var(--pill-blue)" opacity="0.85"/>
      <circle cx="35" cy="227" r="6.5" fill="var(--ink-white)"/>
      <text class="service" x="59" y="237"><tspan class="strong">BEARING PRE-LOAD</tspan><tspan class="light"> TESTING</tspan></text>
    </g>
    <g class="service-item">
      <path d="M9 256 H540 A24 24 0 0 1 540 304 H9 Z" fill="var(--pill-blue)" opacity="0.85"/>
      <circle cx="35" cy="284" r="6.5" fill="var(--ink-white)"/>
      <text class="service" x="59" y="294"><tspan class="strong">BORE</tspan><tspan class="light"> MEASUREMENT</tspan></text>
    </g>
    <g class="service-item">
      <path d="M9 313 H540 A24 24 0 0 1 540 361 H9 Z" fill="var(--pill-blue)" opacity="0.85"/>
      <circle cx="35" cy="341" r="6.5" fill="var(--ink-white)"/>
      <text class="service" x="59" y="351"><tspan class="strong">NEW PRODUCT</tspan><tspan class="light"> EVALUATION</tspan></text>
    </g>
    <g class="service-item">
      <path d="M9 370 H540 A24 24 0 0 1 540 418 H9 Z" fill="var(--pill-blue)" opacity="0.85"/>
      <circle cx="35" cy="398" r="6.5" fill="var(--ink-white)"/>
      <text class="service" x="59" y="408"><tspan class="strong">PRODUCT ANALYSIS</tspan><tspan class="light"> &amp; REPORT</tspan></text>
    </g>
  </g>

  <!-- company name -->
  <g class="company-mark">
    <rect x="27" y="640" width="34" height="34" fill="var(--brand-blue)"/>
    <text class="company-name" x="74" y="669">BOLT REMOVA LTD</text>
  </g>

  <!-- contact bar -->
  <g class="contact-bar">
    <rect x="9" y="767" width="600" height="65" fill="var(--contact-grey)"/>
    <rect x="9" y="767" width="45" height="31" fill="var(--brand-blue-deep)"/>
    <rect x="9" y="801" width="45" height="31" fill="var(--brand-blue-deep)"/>
    <path class="icon-phone" d="M24 774 l4 -1 l3 6 l-3 2 a12 12 0 0 0 6 6 l2 -3 l6 3 l-1 4 a4 4 0 0 1 -4 2 a20 20 0 0 1 -15 -15 a4 4 0 0 1 2 -4 z" fill="var(--ink-white)"/>
    <g class="icon-web" fill="none" stroke="var(--ink-white)" stroke-width="1.8">
      <circle cx="31.5" cy="816.5" r="9"/>
      <ellipse cx="31.5" cy="816.5" rx="4" ry="9"/>
      <line x1="22.5" y1="816.5" x2="40.5" y2="816.5"/>
    </g>
    <text class="phone" x="69" y="795">0161 555 0182</text>
    <text class="web" x="70" y="824">WWW.BOLT-REMOVA.CO.UK</text>
  </g>

  <!-- photo area -->
  <polygon class="workshop-photo" role="img" aria-label="Photo of a technician in safety glasses measuring the bore of a flanged red-painted hub with a digital dial gauge in a workshop"
           points="892,9 1211,9 1211,852 550,852" fill="url(#photoGradient)"/>
</svg>
</body>
</html>
```